Magnetic Business Card Design. One sided

Not happy yet with a design yet currently winning so far are the designs 5162585 5135573 5132280

Logo
unmatched Quality through traditional friendly service" sound like a good line. Blockages, Hot water units & all plumbing services.
7days,
free quote: 0467 215 340
Maybe put on it: Qualified, Licensed
www.brightflowplumbing.com.au

Make word as big so it is clearly able to be read

BrightFlow Plumbing PTY LTD, target market is the middle aged mostly woman professional that owns a house and would rather pay a professional to do the job rather then a handyman.
We are a plumbing company based in Melbourne small and family owned with a focus on service to our customers.

I am after a design that is clean, professional and appealing to the eye which fits with the visual appearance of my web site and logo.

Our most profitable jobs are blockages and hot water units. however we do all types of plumbing. Maybe a point to make on the cards not sure tho.

I have included our previous magnet that i had designed with a pixel press template. if you can improve what we say to get new customers or totally change what is on the magnet. that would be fantastic.

I will also include other marketing material i have previously used

"unmatched Quality Through traditional friendly service" Could be a good catch line

These magnets are dropped into thousands of letter boxes and hopefully will find there way onto new clients fridges. Fridges in million dollar plus houses.

I really look forward to seeing your design. Thank you

Industry/Entity Type

Marketing

Contact Information for Business Card

Number: 0467 215 340
Web site: www.Brightflowplumbing.com.au

```html
<!DOCTYPE html>
<html lang="en">
<head>
<meta charset="utf-8">
<title>BrightFlow Plumbing – Magnet Card</title>
<link rel="stylesheet" href="https://fonts.googleapis.com/css2?family=Arimo:wght@400;700&family=Libre+Baskerville:wght@700&display=swap">
<style>
  :root {
    --navy: #141a4a;
    --blue: #0a5fa8;
    --card-light: #ffffff;
    --card-shade: #dedfe1;
    --backdrop: #2a2b2d;
    --white: #ffffff;
  }
  * { box-sizing: border-box; margin: 0; padding: 0; }
  html, body { width: 1200px; height: 816px; overflow: hidden; }
  body {
    background: var(--backdrop);
    font-family: "Arimo", Arial, sans-serif;
    position: relative;
  }
  .card {
    position: absolute;
    left: 100px; top: 122px;
    width: 1000px; height: 572px;
    border-radius: 10px;
    overflow: hidden;
    background: radial-gradient(ellipse at 55% 40%, var(--card-light) 0%, #f3f3f4 45%, var(--card-shade) 100%);
  }
  .top-band {
    position: absolute; left: 0; top: 0;
    width: 100%; height: 30px;
    background: var(--navy);
    border-bottom-right-radius: 24px;
  }
  .tagline {
    position: absolute; right: 60px; top: 42px;
    color: var(--blue);
    font-size: 19px; letter-spacing: 0.5px;
    text-transform: uppercase;
  }
  .brand {
    position: absolute; left: 150px; top: 120px;
    text-align: center;
    width: 480px;
  }
  .brand .since {
    font-family: "Libre Baskerville", Georgia, serif;
    color: var(--navy); font-size: 16px;
    margin-bottom: 4px;
  }
  .brand .name {
    color: var(--navy);
    font-weight: 700; font-size: 62px;
    line-height: 1;
    letter-spacing: -1px;
  }
  .services {
    position: absolute; left: 600px; top: 190px;
    list-style: none;
  }
  .services li {
    display: flex; align-items: center; gap: 14px;
    color: var(--navy);
    font-weight: 700; font-size: 28px;
    text-transform: uppercase;
    line-height: 1.45;
  }
  .services svg { width: 16px; height: 22px; flex: none; }
  .credentials {
    position: absolute; left: 60px; top: 368px;
    font-family: "Libre Baskerville", Georgia, serif;
    color: var(--blue); font-weight: 700; font-size: 26px;
    text-transform: uppercase; letter-spacing: 0.5px;
  }
  .quote-label {
    position: absolute; left: 62px; top: 410px;
    color: var(--navy); font-size: 32px;
    text-transform: uppercase;
  }
  .phone {
    position: absolute; left: 60px; top: 445px;
    color: var(--navy); font-weight: 700; font-size: 58px;
    letter-spacing: 1px;
  }
  .bottom-band {
    position: absolute; left: 60px; right: 0; bottom: 0;
    height: 62px;
    background: var(--blue);
    border-top-left-radius: 40px;
    display: flex; align-items: center; justify-content: flex-end;
    padding-right: 90px;
  }
  .website {
    color: var(--white); font-weight: 700; font-size: 28px;
  }
</style>
</head>
<body>
  <section class="card" aria-label="BrightFlow Plumbing magnet card">
    <div class="top-band"></div>
    <p class="tagline">Unmatched quality through traditional friendly service</p>

    <div class="brand">
      <p class="since">Since 1980</p>
      <p class="name">BrightFlow Plumbing</p>
    </div>

    <ul class="services">
      <li><svg viewBox="0 0 16 22" aria-hidden="true"><path d="M8 0 C8 6 0 11 0 15 A8 7 0 0 0 16 15 C16 11 8 6 8 0Z" fill="var(--blue)"/></svg>Blockages</li>
      <li><svg viewBox="0 0 16 22" aria-hidden="true"><path d="M8 0 C8 6 0 11 0 15 A8 7 0 0 0 16 15 C16 11 8 6 8 0Z" fill="var(--blue)"/></svg>Hot water units</li>
      <li><svg viewBox="0 0 16 22" aria-hidden="true"><path d="M8 0 C8 6 0 11 0 15 A8 7 0 0 0 16 15 C16 11 8 6 8 0Z" fill="var(--blue)"/></svg>All plumbing services</li>
      <li><svg viewBox="0 0 16 22" aria-hidden="true"><path d="M8 0 C8 6 0 11 0 15 A8 7 0 0 0 16 15 C16 11 8 6 8 0Z" fill="var(--blue)"/></svg>7 days quick</li>
    </ul>

    <p class="credentials">Qualified &amp; Licensed</p>
    <p class="quote-label">Free quote:</p>
    <p class="phone">0467 215 340</p>

    <div class="bottom-band">
      <span class="website">www.brightflowplumbing.com.au</span>
    </div>
  </section>
</body>
</html>
```